professional business card design

Business card design. Photos have been uploaded and i am open to the designer choosing which photos to use. Would like the card to be mostyly in a grey scale design with black, whites, silver & grey colours. I have added copy of our flyer as would like on the back side of card our services to be listed. Do not use any bright colurs such as blue red green or yellow. i need to be able to edit the phone number and naem in the final card design submitted.

Target Market(s)

Clients

Industry/Entity Type

earhmovibng and transport

Contact Information for Business Card

Director Name, address, email, phone number and services

Colors

Designer to choose only greyscale colors for use in the design.

Requirements
Should not have
• no yellow, red, blue or green

```html
<!DOCTYPE html>
<html lang="en">
<head>
<meta charset="UTF-8">
<title>KRV Pty Ltd — Business Card</title>
<link href="https://fonts.googleapis.com/css2?family=Arimo:wght@400;700&display=swap" rel="stylesheet">
<style>
  :root{
    --page:#d9d9d9;
    --ink-black:#0b0b0c;
    --ink-dark:#1a1b1d;
    --ink-mid:#2c2d30;
    --silver:#bfc0c2;
    --silver-light:#e6e6e6;
    --white:#ffffff;
    --grey-text:#b5b5b5;
  }
  *{box-sizing:border-box;margin:0;padding:0}
  html,body{width:1200px;height:800px;overflow:hidden}
  body{
    background:var(--page);
    font-family:"Arimo",Arial,sans-serif;
    display:flex;align-items:center;justify-content:center;gap:40px;
  }
  .card{
    position:relative;width:560px;height:320px;border-radius:18px;overflow:hidden;
    box-shadow:0 12px 30px rgba(0,0,0,.35);
  }

  /* Front */
  .card--front{
    background:linear-gradient(160deg,#2a2b2e 0%,#141517 45%,var(--ink-black) 100%);
  }
  .front__photo{
    position:absolute;left:150px;top:0;width:410px;height:320px;
    background:linear-gradient(110deg,rgba(90,90,95,.0) 0%,#55565a 40%,#3a3b3e 70%,#1c1d20 100%);
    clip-path:polygon(30% 100%,100% 0,100% 38%,55% 100%);
  }
  .front__sheen{
    position:absolute;inset:0;
    background:linear-gradient(200deg,rgba(255,255,255,.08) 0%,rgba(255,255,255,0) 55%);
  }
  .brand{
    position:absolute;left:44px;top:52px;color:var(--silver-light);
    display:flex;align-items:center;gap:12px;
  }
  .brand__mark{width:18px;height:18px;background:var(--silver);}
  .brand__name{font-weight:700;font-size:64px;letter-spacing:2px;line-height:1}
  .brand__suffix{position:absolute;left:44px;top:124px;color:var(--silver);font-size:14px;font-weight:700;letter-spacing:1px}
  .contact-block{
    position:absolute;left:40px;bottom:58px;display:flex;align-items:center;gap:16px;
  }
  .person{text-align:right}
  .person__name{color:var(--white);font-weight:700;font-size:22px;letter-spacing:1px}
  .person__title{color:var(--grey-text);font-size:13px;margin-top:3px}
  .divider{width:1px;height:56px;background:var(--grey-text)}
  .details{list-style:none;color:var(--silver-light);font-size:13px;line-height:19px}
  .details li{display:flex;align-items:center;gap:7px}
  .details svg{width:11px;height:11px;fill:var(--silver-light)}
  .address{position:absolute;left:40px;bottom:26px;color:var(--grey-text);font-size:13px}

  /* Back */
  .card--back{
    background:linear-gradient(180deg,#1e1f22 0%,#0f1012 60%,#2b2c2f 100%);
  }
  .back__band{
    position:absolute;left:0;top:0;width:100%;height:100%;
    background:linear-gradient(180deg,#3a3b3e,#1a1b1d);
    clip-path:polygon(0 0,100% 0,100% 6%,0 30%);
  }
  .services__tab{
    position:absolute;right:0;top:18px;width:250px;height:42px;
    background:linear-gradient(180deg,#8e8f92,#55565a);
    clip-path:polygon(14% 0,100% 0,100% 100%,0 100%);
    color:var(--white);font-weight:700;font-size:22px;
    display:flex;align-items:center;justify-content:flex-end;padding-right:24px;letter-spacing:.5px;
  }
  .services{
    position:absolute;right:22px;top:70px;list-style:none;
    color:var(--white);font-size:13.5px;line-height:17px;text-align:right;
  }
  .services li{display:flex;justify-content:flex-end;align-items:center;gap:8px}
  .services li.services__last{padding-right:20px}
  .services svg{width:12px;height:12px}
  .back__photo{
    position:absolute;left:18px;bottom:0;width:270px;height:170px;
    background:radial-gradient(ellipse at 45% 55%,#cfd0d2 0%,#8a8b8e 45%,#3a3b3e 80%,rgba(40,40,42,0) 100%);
  }
  .back__web{
    position:absolute;right:24px;bottom:12px;color:var(--white);
    font-size:14px;font-weight:700;letter-spacing:6px;line-height:17px;
  }
</style>
</head>
<body>

  <section class="card card--front">
    <div class="front__photo" role="img" aria-label="Photo of a road train with multiple heavy trailers"></div>
    <div class="front__sheen"></div>
    <div class="brand">
      <span class="brand__mark"></span>
      <span class="brand__name">KRV</span>
    </div>
    <div class="brand__suffix">Pty Ltd</div>

    <div class="contact-block">
      <div class="person">
        <div class="person__name">DANIEL HARTLEY</div>
        <div class="person__title">President</div>
      </div>
      <div class="divider"></div>
      <ul class="details">
        <li><svg viewBox="0 0 24 24"><path d="M6.6 10.8a15 15 0 0 0 6.6 6.6l2.2-2.2a1 1 0 0 1 1-.3 11.4 11.4 0 0 0 3.6.6 1 1 0 0 1 1 1V20a1 1 0 0 1-1 1A17 17 0 0 1 3 4a1 1 0 0 1 1-1h3.5a1 1 0 0 1 1 1c0 1.3.2 2.5.6 3.6a1 1 0 0 1-.3 1z"/></svg>555-014-2270</li>
        <li><svg viewBox="0 0 24 24"><path d="M2 5h20v14H2zM3 6l9 7 9-7v1.5l-9 7-9-7z"/></svg>info@krvhaul.com</li>
        <li><svg viewBox="0 0 24 24"><circle cx="12" cy="12" r="10"/></svg>www.krvhaul.com</li>
      </ul>
    </div>
    <div class="address">Depot: Lot 114, Ironbark Range Road, Stonevale</div>
  </section>

  <section class="card card--back">
    <div class="back__band"></div>
    <div class="services__tab">Our Services</div>
    <ul class="services">
      <li>Over size loads / Hot Shot Loads<svg viewBox="0 0 24 24"><circle cx="12" cy="12" r="11" fill="#fff"/><path d="M6.5 12.5l3.5 3.5 7.5-8" stroke="#111" stroke-width="3" fill="none"/></svg></li>
      <li>Heavy Vehicle Recovery services<svg viewBox="0 0 24 24"><circle cx="12" cy="12" r="11" fill="#fff"/><path d="M6.5 12.5l3.5 3.5 7.5-8" stroke="#111" stroke-width="3" fill="none"/></svg></li>
      <li>Potable Water Deliveries<svg viewBox="0 0 24 24"><circle cx="12" cy="12" r="11" fill="#fff"/><path d="M6.5 12.5l3.5 3.5 7.5-8" stroke="#111" stroke-width="3" fill="none"/></svg></li>
      <li>Road Building / Maintenance<svg viewBox="0 0 24 24"><circle cx="12" cy="12" r="11" fill="#fff"/><path d="M6.5 12.5l3.5 3.5 7.5-8" stroke="#111" stroke-width="3" fill="none"/></svg></li>
      <li>Earthworks<svg viewBox="0 0 24 24"><circle cx="12" cy="12" r="11" fill="#fff"/><path d="M6.5 12.5l3.5 3.5 7.5-8" stroke="#111" stroke-width="3" fill="none"/></svg></li>
      <li>Sand &amp; Metal Supply &amp; Cartage<svg viewBox="0 0 24 24"><circle cx="12" cy="12" r="11" fill="#fff"/><path d="M6.5 12.5l3.5 3.5 7.5-8" stroke="#111" stroke-width="3" fill="none"/></svg></li>
      <li>Road Train Tippers<svg viewBox="0 0 24 24"><circle cx="12" cy="12" r="11" fill="#fff"/><path d="M6.5 12.5l3.5 3.5 7.5-8" stroke="#111" stroke-width="3" fill="none"/></svg></li>
      <li>Road Train Tankers<svg viewBox="0 0 24 24"><circle cx="12" cy="12" r="11" fill="#fff"/><path d="M6.5 12.5l3.5 3.5 7.5-8" stroke="#111" stroke-width="3" fill="none"/></svg></li>
      <li>Road Train Flat Tops<svg viewBox="0 0 24 24"><circle cx="12" cy="12" r="11" fill="#fff"/><path d="M6.5 12.5l3.5 3.5 7.5-8" stroke="#111" stroke-width="3" fill="none"/></svg></li>
      <li>Drop Deck Trailers<svg viewBox="0 0 24 24"><circle cx="12" cy="12" r="11" fill="#fff"/><path d="M6.5 12.5l3.5 3.5 7.5-8" stroke="#111" stroke-width="3" fill="none"/></svg></li>
      <li>Mine site accredited<svg viewBox="0 0 24 24"><circle cx="12" cy="12" r="11" fill="#fff"/><path d="M6.5 12.5l3.5 3.5 7.5-8" stroke="#111" stroke-width="3" fill="none"/></svg></li>
      <li class="services__last">Equipment &amp; Operators</li>
    </ul>
    <div class="back__photo" role="img" aria-label="Photo of two prime mover trucks with road train bull bars"></div>
    <div class="back__web">www.krvhaul.com</div>
  </section>

</body>
</html>
```